Managed Service Provider VOIP Flyer

Looking for a one page US letter size single or double sided brochure to offer cloud hosted VoIP Phone system and unified communications. We have partnered with a VoIP Phone system company and want to sell their services but we don't want their name to be shown on the brochure because customers might call them directly. The company name is Quorvel (www.quorvel-example.com) and our company name is Lumen By Harlow, LLC and our voice product is called Clearly Talk. I have also uploaded my company's logo that you should show on the brochure and use that coloring. For more details about the product, you can visit their website mentioned above. Also I am looking for something very similar to this project and many of the technical details are the same https://flyer.contestpad-example.com/contest/5817264

I have also uploaded a PDF with my different package levels and some of the included features. Depending on the design we may or may not want the package levels on this flyer.

Target Market(s)

Small and medium Businesses

Industry/Entity Type

Voip

Requirements
Must have
• Feature and benefits information of Managed VOICE. Use my logo and coloring from my logo. Include our website, email, phone and possibly facebook if it makes sense/looks good.

www.lumenbyharlow-example.com
415.836.0.917
sales@lumenbyharlow-example.com
www.socialsite-example.com/lumenbyharlow
Nice to have
• Would like to show how the service is simple and reliable and available for any business size

```html
<!DOCTYPE html>
<html lang="en">
<head>
<meta charset="utf-8">
<title>Lumen By Harlow – Cloud Based Phone System Flyer</title>
<link rel="stylesheet" href="https://fonts.googleapis.com/css2?family=Titillium+Web:wght@300;400;700;900&family=Open+Sans:wght@400;600;700&family=Arimo:wght@400;700&family=Montserrat:wght@400;500;700&display=swap">
<style>
:root{
  --navy:#1f2a55;
  --navy-deep:#18214a;
  --blue:#3d5d93;
  --red:#8e1c1f;
  --red-dark:#6e1316;
  --red-text:#8b1a1d;
  --grey-dark:#3b3b3d;
  --grey-mid:#6d6f73;
  --ink:#1a1a1a;
  --page:#f1f1f1;
  --white:#ffffff;
}
*{box-sizing:border-box;margin:0;padding:0}
html,body{width:1101px;height:1200px;overflow:hidden;background:var(--page)}
.flyer{
  position:absolute;left:100px;top:18px;width:957px;height:1236px;
  transform:scale(.9404);transform-origin:0 0;
  background:var(--white);overflow:hidden;
  box-shadow:0 4px 18px rgba(0,0,0,.18);
  font-family:"Arimo",Arial,sans-serif;color:var(--ink);
}
.abs{position:absolute}

/* brand */
.brand{left:0;width:957px;top:38px;display:flex;justify-content:center;align-items:center;gap:14px}
.brand-mark{width:34px;height:34px;background:var(--red)}
.brand-name{font-family:"Titillium Web",sans-serif;font-weight:700;font-size:34px;color:var(--navy);letter-spacing:.5px}

/* headline */
.headline{left:0;width:957px;top:118px;text-align:center;font-family:"Titillium Web",sans-serif;font-weight:300;font-size:42px;color:var(--navy);line-height:1.1}
.headline strong{font-weight:700;color:var(--red-text)}
.subline{left:120px;width:717px;top:168px;text-align:center;font-family:"Open Sans",sans-serif;font-size:17px;line-height:24px;color:#3c3c3c}

/* benefits */
.benefit{top:226px;text-align:center}
.benefit svg{display:block;margin:0 auto;height:64px}
.benefit h3{font-family:"Titillium Web",sans-serif;font-weight:700;font-size:21px;margin-top:12px;letter-spacing:.3px}
.benefit p{font-size:13.4px;line-height:16px;text-align:justify;text-align-last:left;margin-top:6px;letter-spacing:-.2px}
.b-voice{left:28px;width:272px}
.b-voice h3{color:var(--navy)}
.b-ease{left:375px;width:210px}
.b-ease h3{color:var(--red-text)}
.b-cost{left:660px;width:272px}
.b-cost h3{color:var(--navy)}

/* features band */
.features-band{left:0;top:428px;width:957px;height:289px;background:linear-gradient(100deg,var(--red-dark) 0%,var(--red) 45%,#7a1a1c 100%)}
.features-tab{left:28px;top:405px;width:272px;height:40px;background:var(--red-dark);border-radius:18px 18px 0 0;color:var(--white);font-family:"Titillium Web",sans-serif;font-weight:700;font-size:24px;padding:4px 0 0 16px;letter-spacing:.3px}
.feature-list{list-style:none;color:var(--white);font-size:17px}
.feature-list li{height:34px;display:flex;align-items:flex-start;gap:8px;position:relative;white-space:nowrap}
.feature-list li::before{content:"";width:11px;height:11px;border:1.6px solid var(--white);margin-top:4px;flex:none;
  background:linear-gradient(45deg,transparent 45%,var(--white) 45%,var(--white) 58%,transparent 58%)}
.feature-list .note{position:absolute;left:84px;top:20px;font-size:9.5px;font-weight:700}
.feature-list .more::before{visibility:hidden}
.fl-1{left:28px;top:454px}
.fl-2{left:260px;top:454px}

.addons{left:530px;top:460px;width:300px;height:185px;background:var(--navy);border-radius:8px 0 0 8px;padding:16px 0 0 24px;color:var(--white)}
.addons h4{font-family:"Open Sans",sans-serif;font-weight:700;font-size:22px;margin-bottom:14px}
.addons ul{list-style:none}
.addons li{font-family:"Open Sans",sans-serif;font-weight:700;font-size:15.5px;height:29px;display:flex;align-items:center;gap:8px;letter-spacing:.3px}
.addons li svg{width:14px;height:14px}
.rep-photo{left:760px;top:408px;width:197px;height:309px;background:linear-gradient(180deg,#b9c7da 0%,#7e96b8 60%,#5d7699 100%)}

/* plans */
.plans{left:0;top:717px;width:957px;height:445px;background:linear-gradient(90deg,#ececec 0%,#d7d7d7 40%,#bdbdbd 70%,#d9d9d9 100%)}
.plans-photo{left:180px;top:760px;width:420px;height:380px;background:radial-gradient(ellipse at 50% 50%,rgba(150,150,150,.45),rgba(200,200,200,0) 70%)}
.plans-title{left:0;width:957px;top:728px;text-align:center;font-family:"Titillium Web",sans-serif;font-weight:700;font-size:31px;color:var(--red-text);letter-spacing:.6px}
.plan-rule{left:25px;top:778px;width:8px;height:370px;background:var(--navy)}
.plan-rule::after{content:"";position:absolute;left:9px;top:0;width:2px;height:100%;background:var(--blue)}
.plan-list{list-style:none;font-family:"Montserrat",sans-serif;font-size:14.2px;color:#2b2b2b;letter-spacing:.1px}
.plan-list li{display:block;height:16px;line-height:16px;white-space:nowrap;overflow:visible}
.plan-list li::before{content:"✓";font-size:10px;line-height:16px;margin-right:6px;font-family:"Arimo",sans-serif}
.pl-1{left:55px;top:777px}
.pl-2{left:55px;top:921px}
.pl-3{left:55px;top:1097px}
.plan-table{left:410px;top:778px;width:527px;height:372px}
.plan-head{color:var(--white);text-align:center;width:170px}
.plan-head .name{font-family:"Open Sans",sans-serif;font-weight:700;font-size:17px;letter-spacing:.2px}
.plan-head .who{font-family:"Open Sans",sans-serif;font-size:13px;margin-top:14px}
.plan-head .price{font-family:"Montserrat",sans-serif;font-size:36px;margin-top:10px;font-weight:700}
.ph-primer{left:415px;top:796px}
.ph-standard{left:578px;top:796px}
.ph-premium{left:747px;top:796px}
.plus{color:var(--white);font-family:"Arimo",sans-serif;font-weight:700;font-size:42px;width:40px;text-align:center;line-height:1}

/* footer */
.visit-tab{left:0;top:1160px;width:240px;height:32px;background:var(--navy);clip-path:polygon(0 0,220px 0,240px 100%,0 100%);color:var(--white);font-size:13px;padding:9px 0 0 28px;display:flex;gap:10px}
.visit-tab i{display:inline-block;width:15px;height:15px;background:var(--white);border-radius:2px;margin-top:-1px}
.footer-bar{left:0;top:1191px;width:957px;height:45px;background:var(--red)}
.site{left:27px;top:1197px;font-family:"Open Sans",sans-serif;font-size:22px;letter-spacing:1.5px;color:var(--white);white-space:nowrap}
.contact-tab{left:420px;top:1158px;width:190px;height:35px;background:#d0d0d0;clip-path:polygon(14px 0,100% 0,176px 100%,0 100%);font-family:"Open Sans",sans-serif;font-size:21px;color:#222;padding:3px 0 0 24px;white-space:nowrap}
.contact-box{left:575px;top:1154px;width:363px;height:82px;background:var(--navy);clip-path:polygon(28px 0,100% 0,100% 100%,0 100%);color:var(--white);font-family:"Open Sans",sans-serif}
.phone{position:absolute;left:64px;top:4px;font-family:"Titillium Web",sans-serif;font-weight:700;font-size:34px;letter-spacing:.5px;display:flex;align-items:center;gap:10px;white-space:nowrap}
.email{position:absolute;left:40px;top:50px;font-size:15.5px;display:flex;align-items:center;gap:12px;white-space:nowrap}
</style>
</head>
<body>
<div class="flyer">

  <div class="abs brand">
    <span class="brand-mark"></span>
    <span class="brand-name">Lumen By Harlow</span>
  </div>

  <h1 class="abs headline"><strong>A Cloud Based</strong> Phone system For Businesses</h1>
  <p class="abs subline">Simple and smart communication services enabling businesses to communicate whenever, wherever and however they want.</p>

  <section class="abs benefit b-voice">
    <svg viewBox="0 0 60 64" fill="none" stroke="#1f2a55" stroke-width="2.2">
      <rect x="24" y="2" width="12" height="22" rx="6"/>
      <path d="M19 18c0 8 5 12 11 12s11-4 11-12M30 30v8"/>
      <path d="M6 52v6M10 48v14M14 50v10M18 44v20M22 48v12M26 42v22M30 46v14M34 42v22M38 48v12M42 44v20M46 50v10M50 48v14M54 52v6"/>
    </svg>
    <h3>HIGH QUALITY VOICE</h3>
    <p>Largest on-net phone number footprint in the US with 90%+ of calls originating and terminating on-net, achieving industry leading 97% call completion.</p>
  </section>

  <section class="abs benefit b-ease">
    <svg viewBox="0 0 70 64" fill="none" stroke="#1f2a55" stroke-width="2.2">
      <path d="M12 20a24 24 0 0 1 40-10M58 40a24 24 0 0 1-40 12"/>
      <circle cx="35" cy="26" r="9"/>
      <path d="M22 50c2-8 8-12 13-12s11 4 13 12"/>
      <path d="M25 26a10 10 0 0 1 20 0"/>
      <path d="M10 44l6 6 6-4-3-5" stroke="#8e1c1f"/>
      <rect x="52" y="2" width="14" height="10" rx="3" stroke="#3d5d93"/>
    </svg>
    <h3>EASE OF USE</h3>
    <p>100% self-service via our Admin Portal and backed by Local Minnesota Support.</p>
  </section>

  <section class="abs benefit b-cost">
    <svg viewBox="0 0 64 64" fill="none" stroke="#1f2a55" stroke-width="2.2">
      <path d="M12 22a22 22 0 0 1 32-12M52 42a22 22 0 0 1-32 12"/>
      <circle cx="32" cy="32" r="10"/>
      <circle cx="32" cy="32" r="4"/>
      <path d="M32 18v4M32 42v4M18 32h4M42 32h4M22 22l3 3M39 39l3 3M42 22l-3 3M22 42l3-3"/>
      <circle cx="12" cy="14" r="7"/><circle cx="52" cy="50" r="7"/>
      <path d="M12 10v8M52 46v8" stroke-width="1.6"/>
    </svg>
    <h3>COST-EFFECTIVE</h3>
    <p>As a Tier 1 Carrier, we help you eliminate the middleman and saving your business 20-40% on your existing communication service.</p>
  </section>

  <div class="abs features-band"></div>
  <div class="abs features-tab">INCLUDED FEATURES</div>

  <ul class="abs feature-list fl-1">
    <li>Auto Attendant</li>
    <li>Ring/hunt groups</li>
    <li>Extensions</li>
    <li>Caller-ID</li>
    <li>Call Transfer/Forwarding</li>
    <li>Conference Rooms</li>
    <li>Call parking</li>
  </ul>
  <ul class="abs feature-list fl-2">
    <li>Voicemail/Voicemail to email</li>
    <li>Time Conditions</li>
    <li>Detailed Call Reports</li>
    <li>Virtual/Local Numbers<span class="note">(Free Number Porting)</span></li>
    <li>Do Not Disturb</li>
    <li>Toll Free Numbers</li>
    <li>Local Minnesota Support</li>
    <li class="more">And More!</li>
  </ul>

  <div class="abs addons">
    <h4>Add-On Features:</h4>
    <ul>
      <li><svg viewBox="0 0 14 14"><path d="M3 2l6 5-6 5" fill="none" stroke="#fff" stroke-width="2.4"/></svg>CALL RECORDING</li>
      <li><svg viewBox="0 0 14 14"><path d="M3 2l6 5-6 5" fill="none" stroke="#fff" stroke-width="2.4"/></svg>CALL CENTER</li>
      <li><svg viewBox="0 0 14 14"><path d="M3 2l6 5-6 5" fill="none" stroke="#fff" stroke-width="2.4"/></svg>HOSTED FAX</li>
      <li><svg viewBox="0 0 14 14"><path d="M3 2l6 5-6 5" fill="none" stroke="#fff" stroke-width="2.4"/></svg>VIRTUAL NUMBERS</li>
    </ul>
  </div>
  <div class="abs rep-photo" role="img" aria-label="Smiling representative in a blue shirt holding a desk phone"></div>

  <div class="abs plans"></div>
  <div class="abs plans-photo" role="img" aria-label="Faded photo of a hand dialing a desk phone keypad"></div>
  <h2 class="abs plans-title">CHOOSE THE BEST PHONE PLAN FOR YOUR BUSINESS</h2>

  <div class="abs plan-rule"></div>
  <ul class="abs plan-list pl-1">
    <li>EXTENSION DIALING</li>
    <li>LOCAL OUTBOUND CALLS ONLY</li>
    <li>CALLER ID AND CALLER NAME</li>
    <li>CALL LOGS</li>
    <li>LAST NUMBER DIAL</li>
    <li>MUSIC ON HOLD</li>
    <li>CORPORATE DIRECTORY ACCESS</li>
    <li>E911 SERVICE</li>
  </ul>
  <ul class="abs plan-list pl-2">
    <li>CALL PARK</li>
    <li>CALL FORWARDING</li>
    <li>UNLIMITED LONG DISTANCE</li>
    <li>CALL TRANSFER</li>
    <li>CALL WAITING</li>
    <li>UNIFIED MESSAGING</li>
    <li>INCLUSION IN HUNT GROUPS</li>
    <li>SIMULTANEOUS RING</li>
    <li>SPEED DIAL 100</li>
    <li>THREE-WAY CALLING</li>
  </ul>
  <ul class="abs plan-list pl-3">
    <li>MOBILE CLIENT</li>
    <li>DESKTOP SHARING</li>
    <li>WEB COLLABORATION</li>
  </ul>

  <svg class="abs plan-table" viewBox="410 778 527 372">
    <polygon points="935,778 722,778 748,845 735,912 760,1000 735,1082 735,1148 935,1148" fill="#1f2a55"/>
    <polygon points="735,1082 935,1082 935,1148 735,1148" fill="#2a3562"/>
    <polygon points="590,778 722,778 748,845 722,912 590,912" fill="#1e2b58"/>
    <polygon points="590,778 722,778 748,845 722,912 590,912" fill="#3d5d93" opacity=".55"/>
    <polygon points="596,912 735,912 760,1000 735,1082 596,1082 572,1000" fill="#3d5d93"/>
    <polygon points="440,778 590,778 614,845 590,912 415,912 415,845" fill="#3b3b3d"/>
  </svg>

  <div class="abs plan-head ph-primer"><div class="name">PRIMER</div><div class="who">(Location, not a user)</div><div class="price">$ 20</div></div>
  <div class="abs plan-head ph-standard"><div class="name">STANDARD</div><div class="who">(Basic user)</div><div class="price">$ 30</div></div>
  <div class="abs plan-head ph-premium"><div class="name">PREMIUM</div><div class="who">(Power user)</div><div class="price">$ 35</div></div>

  <div class="abs plus" style="left:640px;top:974px">+</div>
  <div class="abs plus" style="left:818px;top:974px">+</div>
  <div class="abs plus" style="left:818px;top:1094px">+</div>

  <div class="abs visit-tab">VISIT US AT <i></i></div>
  <div class="abs footer-bar"></div>
  <div class="abs site">www.lumenbyharlow-example.com</div>
  <div class="abs contact-tab">CONTACT US</div>
  <div class="abs contact-box">
    <div class="phone">
      <svg width="30" height="30" viewBox="0 0 30 30" fill="none" stroke="#fff" stroke-width="2.2"><circle cx="15" cy="15" r="13"/><path d="M10 8l3 3-2 3c1 2 3 4 5 5l3-2 3 3-2 3c-6 0-12-6-12-12z" fill="#fff" stroke="none"/></svg>
      415.836.0917
    </div>
    <div class="email">
      <svg width="20" height="15" viewBox="0 0 20 15"><rect width="20" height="15" rx="1.5" fill="#fff"/><path d="M1 1l9 7 9-7" fill="none" stroke="#1f2a55" stroke-width="1.6"/></svg>
      sales@lumenbyharlow-example.com
    </div>
  </div>

</div>
</body>
</html>
```